Banner poster with different motifs

I'm looking for 5 banners and posters in A1 format in the same design, or the similarity must be recognizable...
Kept quite simple with different titles.

1 ballet
2 Contemporary Dance
3 high heels
4 Salsa & Bachata & Zouk
5 Hip Hop

Modern bright colors
it is for the entrance so that the students see here is a dance school

The text may also be included in the image
The photos are for guidance only; some are our own, some are purchased. However, we are permitted to use them, including our logo, of course.

```html
<!DOCTYPE html>
<html lang="en">
<head>
<meta charset="utf-8">
<title>VELARO Dance Classes</title>
<link href="https://fonts.googleapis.com/css2?family=Bebas+Neue&display=swap" rel="stylesheet">
<style>
  :root {
    --sheet: #ffffff;
    --ink: #050505;
    --magenta: #e0118a;
    --magenta-deep: #b3135f;
    --rose: #d0287a;
    --violet: #6a1a9a;
    --white: #ffffff;
  }
  * { box-sizing: border-box; margin: 0; padding: 0; }
  html, body { width: 934px; height: 1200px; overflow: hidden; }
  body {
    background: var(--sheet);
    font-family: "Bebas Neue", "Oswald", sans-serif;
    position: relative;
  }
  .panel { position: absolute; overflow: hidden; }
  .panel--ballet { left: 30px; top: 32px; width: 427px; height: 401px;
    background: linear-gradient(180deg, var(--ink) 30%, var(--magenta-deep) 75%, var(--magenta) 100%); }
  .panel--contemporary { left: 476px; top: 32px; width: 428px; height: 401px;
    background: radial-gradient(ellipse at 40% 70%, var(--violet) 0%, #3a0d4f 40%, var(--ink) 80%); }
  .panel--latin { left: 30px; top: 448px; width: 874px; height: 308px;
    background: var(--ink); }
  .panel--heels { left: 30px; top: 771px; width: 427px; height: 401px;
    background: linear-gradient(135deg, var(--magenta-deep) 0%, var(--rose) 55%, var(--magenta) 100%); }
  .panel--hiphop { left: 476px; top: 771px; width: 428px; height: 401px;
    background: linear-gradient(180deg, var(--ink) 45%, var(--magenta-deep) 80%, var(--magenta) 100%); }

  .photo { position: absolute; border-radius: 40% 40% 30% 30%; }
  .panel--ballet .photo { left: 150px; top: 40px; width: 255px; height: 340px;
    background: radial-gradient(ellipse, rgba(40,20,30,.75) 0%, rgba(40,20,30,0) 70%); }
  .panel--contemporary .photo { left: 60px; top: 110px; width: 350px; height: 280px;
    background: radial-gradient(ellipse, rgba(200,150,130,.35) 0%, rgba(200,150,130,0) 70%); }
  .panel--latin .smoke { position: absolute; left: 0; top: 0; width: 874px; height: 90px;
    background: radial-gradient(ellipse at 60% 0%, rgba(224,17,138,.55) 0%, rgba(224,17,138,0) 70%); }
  .panel--latin .photo { left: 470px; top: 10px; width: 380px; height: 290px;
    background: radial-gradient(ellipse, rgba(200,170,150,.4) 0%, rgba(200,170,150,0) 70%); }
  .panel--heels .photo { left: 160px; top: 30px; width: 240px; height: 360px;
    background: radial-gradient(ellipse, rgba(60,20,30,.45) 0%, rgba(60,20,30,0) 70%); }
  .panel--hiphop .photo { left: 200px; top: 20px; width: 210px; height: 370px;
    background: radial-gradient(ellipse, rgba(120,80,60,.4) 0%, rgba(120,80,60,0) 70%); }

  .title { position: absolute; line-height: .86; color: var(--white); letter-spacing: 1px; }
  .title .accent { color: var(--magenta); }
  .title span { display: block; }
  .panel--ballet .title { left: 27px; top: 33px; font-size: 90px; }
  .panel--contemporary .title { left: 20px; top: 25px; font-size: 68px; }
  .panel--latin .title { left: 27px; top: 112px; font-size: 90px; }
  .panel--heels .title { left: 27px; top: 27px; }
  .panel--heels .title .big { font-size: 162px; }
  .panel--heels .title .small { font-size: 66px; }
  .panel--hiphop .title { left: 25px; top: 27px; font-size: 162px; line-height: .78; }
  .panel--hiphop .title .gap { margin-top: 8px; }

  .brand { position: absolute; display: flex; flex-direction: column; align-items: center; gap: 6px; color: var(--white); }
  .brand .dot { width: 34px; height: 34px; border: 1.5px solid var(--white); border-radius: 50%; }
  .brand .name { font-size: 22px; letter-spacing: 4px; line-height: 1; }
  .panel--ballet .brand { left: 285px; top: 45px; }
  .panel--contemporary .brand { left: 25px; top: 305px; }
  .panel--latin .brand { left: 28px; top: 30px; }
  .panel--heels .brand { left: 25px; top: 300px; }
  .panel--hiphop .brand { left: 25px; top: 300px; }
</style>
</head>
<body>
  <section class="panel panel--ballet">
    <div class="photo" role="img" aria-label="Ballerina in black leotard on pointe, arching back"></div>
    <h2 class="title"><span class="accent">Ballet</span><span>Dance</span></h2>
    <div class="brand"><div class="dot"></div><div class="name">VELARO</div></div>
  </section>

  <section class="panel panel--contemporary">
    <div class="photo" role="img" aria-label="Contemporary dancer leaping in a split jump over violet smoke"></div>
    <h2 class="title"><span>Contemporary</span><span class="accent">Dance</span></h2>
    <div class="brand"><div class="dot"></div><div class="name">VELARO</div></div>
  </section>

  <section class="panel panel--latin">
    <div class="smoke" role="img" aria-label="Magenta smoke swirls"></div>
    <div class="photo" role="img" aria-label="Two dance couples in partner poses"></div>
    <div class="brand"><div class="dot"></div><div class="name">VELARO</div></div>
    <h2 class="title"><span>Salsa and</span><span class="accent">Bachata &amp; Zouk</span></h2>
  </section>

  <section class="panel panel--heels">
    <div class="photo" role="img" aria-label="Dancer in black outfit and high heels crouching"></div>
    <h2 class="title"><span class="big">High</span><span class="small">Heels</span></h2>
    <div class="brand"><div class="dot"></div><div class="name">VELARO</div></div>
  </section>

  <section class="panel panel--hiphop">
    <div class="photo" role="img" aria-label="Hip hop dancer in black mid-jump"></div>
    <h2 class="title"><span class="accent">Hip</span><span class="gap">Hop</span></h2>
    <div class="brand"><div class="dot"></div><div class="name">VELARO</div></div>
  </section>
</body>
</html>
```